Small business that sells dolls used in the investigation of sudden infant deaths needs a website de

We need a modern update to our very simple current website. We are a small business that manufactures and sells featureless dolls used in the training and investigation of sudden infant deaths. With our customer base being primarily government organizations we are looking for design that is to the point and functional while also being engaging.

Target Market(s)

Our target audience are organizations such as government offices and training organizations looking for information about our product. This makes readability and ease-of-use of the design very important.

Number of Pages Required

5+ page

Font styles to use
Serif

Colors

Designer to choose colors to be used in the design.

Requirements
Must have
• Straightforward website focused towards the product being sold. With secondary focus is being how to contact the business and the care and use of the product. The business logo is orange and blue, these colors do not necessarily need to show up in the website design. Darker and muted/contrasting colors would probably be better.
Nice to have
• It would be nice if the website had a professional feel, that is slightly maternal but is not cutesy. Given the nature of our product, we also would like a site that is very respectful for any case that our product might be used in it.

```html
<!DOCTYPE html>
<html lang="en">
<head>
<meta charset="utf-8">
<title>Gentle Hands Study Dolls</title>
<link href="https://fonts.googleapis.com/css2?family=Montserrat:wght@500;600;700;800&family=Poppins:wght@400;500;600&display=swap" rel="stylesheet">
<style>
:root{
  --orange:#e8401c;
  --blue:#2f8be6;
  --ink:#111418;
  --body:#3a3d42;
  --muted:#6b6f75;
  --footer:#0e1822;
  --white:#ffffff;
}
*{margin:0;padding:0;box-sizing:border-box}
html,body{width:1200px;height:3403px;overflow:hidden;background:var(--white)}
body{position:relative;font-family:'Poppins',sans-serif;color:var(--body)}
.abs{position:absolute}
.brand{left:85px;top:52px;display:flex;align-items:center;gap:16px}
.brand-dot{width:56px;height:56px;border-radius:50%;background:var(--blue)}
.brand-name{font-family:'Montserrat',sans-serif;font-weight:700;font-size:24px;line-height:29px;color:var(--ink)}
.hero-photo{left:490px;top:-290px;width:980px;height:980px;border-radius:50%;border:12px solid var(--orange);background:radial-gradient(circle at 55% 60%,#e26a6a,#b8474d 45%,#3b3a3a 80%);box-shadow:inset 0 0 0 6px var(--blue)}
.nav{top:56px;left:662px;display:flex;font-family:'Montserrat',sans-serif;font-weight:700;font-size:20px;color:var(--white)}
.nav a{color:inherit;text-decoration:none;display:block;width:130px;text-align:center;line-height:32px}
.nav .current{width:80px;height:80px;border:3px solid rgba(255,255,255,.8);border-radius:50%;line-height:74px;margin-top:-22px;margin-right:25px}
.hero-title{left:85px;top:255px;width:420px;font-family:'Montserrat',sans-serif;font-weight:600;font-size:38px;line-height:50px;color:var(--ink)}
.btn{display:block;background:var(--orange);color:var(--white);font-family:'Montserrat',sans-serif;font-weight:700;font-size:16px;letter-spacing:1px;text-align:center;line-height:50px;height:50px;box-shadow:6px 6px 0 var(--blue);text-decoration:none}
.hero-btn{left:85px;top:493px;width:175px}
.eyebrow{left:0;width:1200px;text-align:center;font-family:'Montserrat',sans-serif;font-weight:700;font-size:19px;color:var(--ink)}
.section-title{left:0;width:1200px;text-align:center;font-family:'Montserrat',sans-serif;font-weight:600;font-size:48px;color:var(--orange);letter-spacing:1px}
.intro{left:120px;width:960px;top:895px;text-align:center;font-size:16px;line-height:30px;color:var(--body)}
.intro .motto{color:var(--orange);font-weight:500}
.point{width:240px;text-align:center}
.point h3{font-family:'Montserrat',sans-serif;font-weight:700;font-size:14px;color:var(--ink);margin-bottom:10px;letter-spacing:.5px}
.point p{font-size:15px;line-height:24px;color:var(--muted)}
.hub{left:484px;top:1180px;width:226px;height:226px;border-radius:50%;border:14px solid var(--blue);display:flex;align-items:center;justify-content:center;font-family:'Montserrat',sans-serif;font-weight:700;font-size:20px;color:var(--orange);text-align:center;line-height:26px}
.doll-photo{left:125px;top:1733px;width:432px;height:432px;border-radius:50%;background:var(--orange)}
.doll-photo-blue{left:119px;top:1726px;width:430px;height:430px;border-radius:50%;background:var(--blue)}
.doll-photo-inner{left:112px;top:1720px;width:428px;height:428px;border-radius:50%;background:radial-gradient(circle at 50% 50%,#dcdcdc,#9a9a9a 30%,#0b0b0b 55%)}
.order-label{left:635px;top:1745px;font-family:'Montserrat',sans-serif;font-weight:700;font-size:20px;color:var(--ink)}
.price-table{left:638px;top:1795px;width:474px;border-collapse:collapse;border:3px solid var(--ink)}
.price-table td{border:2px solid var(--ink);height:68px;text-align:center;font-family:'Montserrat',sans-serif;font-weight:700;font-size:14px;line-height:24px;color:var(--ink)}
.price-table .size{color:var(--orange);width:120px}
.price-table .price{color:var(--orange)}
.ship-title{left:638px;top:1968px;font-family:'Montserrat',sans-serif;font-weight:700;font-size:21px;color:var(--ink)}
.ship-line{left:640px;font-size:21px;color:var(--muted)}
.order-btn{left:646px;top:2102px;width:175px}
.feature{width:300px;text-align:center}
.feature h3{font-family:'Montserrat',sans-serif;font-weight:600;font-size:21px;color:var(--ink);margin-bottom:14px}
.feature p{width:250px;margin:0 auto;font-size:14px;line-height:24px;color:var(--body)}
.footer{left:0;top:2872px;width:1200px;height:531px;background:var(--footer)}
.cta{left:105px;top:2822px;width:997px;height:96px;background:var(--orange);display:flex;align-items:center;padding-left:30px}
.cta-ask{margin-left:20px;font-family:'Montserrat',sans-serif;font-weight:700;font-size:14px;line-height:16px;color:var(--white)}
.cta-phone{margin-left:14px;font-family:'Montserrat',sans-serif;font-weight:800;font-size:36px;color:var(--white);letter-spacing:1px}
.cta-input{left:552px;top:24px;width:270px;height:36px;border-radius:18px;background:var(--white);display:flex;align-items:center;padding-left:18px;gap:14px;font-size:13px;font-style:italic;color:#888}
.cta-btn{left:840px;top:24px;width:133px;height:36px;border-radius:18px;background:var(--blue);color:var(--white);font-family:'Montserrat',sans-serif;font-weight:700;font-size:15px;text-align:center;line-height:36px}
.foot-mark{left:128px;top:3000px;width:240px;height:240px;border-radius:50%;border:12px solid var(--white);display:flex;align-items:center;justify-content:center;font-family:'Montserrat',sans-serif;font-weight:700;font-size:22px;line-height:30px;text-align:center;color:var(--white)}
.foot-head{font-family:'Montserrat',sans-serif;font-weight:600;font-size:16px;color:var(--white);letter-spacing:1px}
.foot-list{list-style:none;font-size:15px;color:var(--white)}
.quick li{display:flex;align-items:center;gap:16px;height:31px}
.quick li::before{content:"";width:12px;height:12px;border-radius:50%;background:var(--white)}
.social li{height:47px}
.contact-item{display:flex;gap:14px;width:240px}
.contact-item .ico{flex:none;width:22px;height:22px;border-radius:50%;background:var(--orange)}
.contact-item b{display:block;font-weight:500;font-size:14px;color:var(--orange)}
.contact-item span{display:block;font-size:14px;line-height:17px;color:var(--white)}
.rule{left:85px;top:3335px;width:1030px;height:1px;background:rgba(255,255,255,.5)}
.copy{left:0;width:1200px;top:3358px;text-align:center;font-size:13px;color:var(--white)}
</style>
</head>
<body>

<header>
  <div class="hero-photo abs" role="img" aria-label="Photo of many red-orange cloth investigation dolls laid out on a table"></div>
  <div class="brand abs"><span class="brand-dot"></span><span class="brand-name">Gentle Hands<br>Study Dolls</span></div>
  <nav class="nav abs"><a class="current" href="#">HOME</a><a href="#">ABOUT</a><a href="#">ORDER</a><a href="#">CONTACT</a></nav>
  <h1 class="hero-title abs">Investigation Dolls<br>For Sudden,<br>Unexplained<br>Infant Death</h1>
  <a class="btn hero-btn abs" href="#">ORDER NOW</a>
</header>

<section class="welcome">
  <p class="eyebrow abs" style="top:773px">WELCOME TO</p>
  <h2 class="section-title abs" style="top:808px">GENTLE HANDS STUDY DOLLS</h2>
  <p class="intro abs">Our partnership started with a quilt for a newborn baby that was found in a plastic bag in our community.&nbsp; Her quilt, along with several others, was taken to our county coroner, who told others of our mission to<br><span class="motto">"Use the talents the Lord gave us to help others."</span></p>
</section>

<section class="qualities">
  <svg class="abs" style="left:0;top:1140px" width="1200" height="300" viewBox="0 0 1200 300">
    <g fill="none" stroke="#555" stroke-width="2">
      <polyline points="320,20 462,20 462,70"/>
      <polyline points="880,20 730,20 730,70"/>
      <polyline points="320,290 462,290 462,237"/>
      <polyline points="880,290 730,290 730,237"/>
    </g>
    <g fill="#e8401c"><circle cx="462" cy="72" r="7"/><circle cx="730" cy="72" r="7"/><circle cx="462" cy="235" r="7"/><circle cx="730" cy="235" r="7"/></g>
  </svg>
  <div class="hub abs">Gentle<br>Hands</div>
  <div class="point abs" style="left:86px;top:1097px"><h3>SAFETY</h3><p>Lorem Ipsum is simply dummy text of the printing and typesetting industry.</p></div>
  <div class="point abs" style="left:874px;top:1097px"><h3>WATER REPELLENTS</h3><p>Lorem Ipsum is simply dummy text of the printing and typesetting industry.</p></div>
  <div class="point abs" style="left:86px;top:1380px"><h3>GOOD SHAPE</h3><p>Lorem Ipsum is simply dummy text of the printing and typesetting industry.</p></div>
  <div class="point abs" style="left:874px;top:1380px"><h3>LIGHT COLORED</h3><p>Lorem Ipsum is simply dummy text of the printing and typesetting industry.</p></div>
</section>

<section class="order">
  <p class="eyebrow abs" style="top:1568px">BUY NOW</p>
  <h2 class="section-title abs" style="top:1603px">ORDER INFORMATION</h2>
  <div class="doll-photo abs"></div>
  <div class="doll-photo-blue abs"></div>
  <div class="doll-photo-inner abs" role="img" aria-label="Photo of a white featureless cloth doll on a black background"></div>
  <p class="order-label abs">STUDY DOLLS:</p>
  <table class="price-table abs">
    <tr><td class="size">6 LB.<br>DOLLS</td><td>WHITE<br><span class="price">$39.00</span></td><td>ORANGE<br><span class="price">$41.00</span></td></tr>
    <tr><td class="size">8 LB.<br>DOLLS</td><td>WHITE<br><span class="price">$40.00</span></td><td>ORANGE<br><span class="price">$42.00</span></td></tr>
  </table>
  <p class="ship-title abs">Shipping &amp; handling:</p>
  <p class="ship-line abs" style="top:2008px">1 - 2 dolls: $13.60</p>
  <p class="ship-line abs" style="top:2046px">3 dolls: $18.85</p>
  <a class="btn order-btn abs" href="#">ORDER FORM</a>
</section>

<section class="features">
  <p class="eyebrow abs" style="top:2278px">BENEFITS</p>
  <h2 class="section-title abs" style="top:2313px">OUR FEATURES</h2>
  <svg class="abs" style="left:0;top:2440px" width="1200" height="150" viewBox="0 0 1200 150">
    <g stroke="#888" stroke-width="3" stroke-dasharray="2 7"><line x1="335" y1="70" x2="505" y2="70"/><line x1="685" y1="70" x2="855" y2="70"/></g>
    <g fill="none" stroke="#2f8be6" stroke-width="3">
      <circle cx="265" cy="70" r="60"/><circle cx="615" cy="70" r="60"/><circle cx="965" cy="70" r="60"/>
    </g>
    <g font-family="Montserrat, sans-serif" font-weight="800" font-size="120" fill="#fff" stroke="#2f8be6" stroke-width="3">
      <text x="160" y="115">1</text><text x="510" y="115">2</text><text x="855" y="115">3</text>
    </g>
    <g fill="#e8401c">
      <ellipse cx="265" cy="70" rx="26" ry="22"/>
      <path d="M615 38 L630 70 A16 16 0 1 1 600 70 Z"/>
      <rect x="956" y="40" width="18" height="52" rx="3"/>
    </g>
    <g fill="#fff"><circle cx="256" cy="62" r="4"/><circle cx="272" cy="60" r="4"/><circle cx="277" cy="75" r="4"/></g>
  </svg>
  <div class="feature abs" style="left:100px;top:2588px"><h3>COLOR OPTIONS</h3><p>The six or eight pound featureless dolls are made of light-colored fabric or orange high-visibility fabric for photographic purposes.</p></div>
  <div class="feature abs" style="left:450px;top:2588px"><h3>GERMICIDAL SOLUTION</h3><p>The orange fabric may be wiped with a germicidal solution using a damp rag.</p></div>
  <div class="feature abs" style="left:800px;top:2588px"><h3>MARKER</h3><p>A permanent marker may be used to mark the front and back or add facial features as desired.</p></div>
</section>

<footer>
  <div class="footer abs"></div>
  <div class="cta abs">
    <svg width="34" height="34" viewBox="0 0 24 24"><path fill="#fff" d="M6.6 10.8a15.1 15.1 0 0 0 6.6 6.6l2.2-2.2a1 1 0 0 1 1-.25 11.4 11.4 0 0 0 3.6.57 1 1 0 0 1 1 1V20a1 1 0 0 1-1 1A17 17 0 0 1 3 4a1 1 0 0 1 1-1h3.5a1 1 0 0 1 1 1c0 1.25.2 2.45.57 3.57a1 1 0 0 1-.25 1z"/></svg>
    <p class="cta-ask">DO YOU HAVE<br>A QUESTION?</p>
    <p class="cta-phone">+0100 555 0199</p>
    <div class="cta-input abs"><svg width="14" height="11" viewBox="0 0 14 11"><rect width="14" height="11" rx="1" fill="#999"/><path d="M1 1l6 5 6-5" stroke="#fff" fill="none"/></svg>Enter your email address</div>
    <div class="cta-btn abs">Subscribe</div>
  </div>

  <div class="foot-mark abs">Gentle<br>Hands</div>

  <p class="foot-head abs" style="left:470px;top:3003px">QUICK LINKS</p>
  <ul class="foot-list quick abs" style="left:472px;top:3040px">
    <li>Home</li><li>About</li><li>Products</li><li>Features</li><li>Testimonials</li><li>Contact</li>
  </ul>

  <p class="foot-head abs" style="left:693px;top:3003px">FOLLOW US</p>
  <ul class="foot-list social abs" style="left:693px;top:3045px">
    <li>Facebook</li><li>Instagram</li><li>Twitter</li><li>LinkedIn</li>
  </ul>

  <p class="foot-head abs" style="left:876px;top:3003px">CONTACT US</p>
  <div class="contact-item abs" style="left:876px;top:3046px"><span class="ico"></span><div><b>Head Office</b><span>123, Main Street, Your City<br>USA 789456</span></div></div>
  <div class="contact-item abs" style="left:876px;top:3142px"><span class="ico"></span><div><b>Phone Number</b><span>+123 456 7890<br>+123 456 7890</span></div></div>
  <div class="contact-item abs" style="left:876px;top:3228px"><span class="ico"></span><div><b>Email</b><span>hello@gentlehandsdolls.com<br>www.gentlehandsdolls.com</span></div></div>

  <div class="rule abs"></div>
  <p class="copy abs">Copyright © 2019, All Rights Reserved.</p>
</footer>

</body>
</html>
```